Lounge Night Poster

We need an attractive poster for our new lounge/night club in San Francisco called Velora Nightclub, promoting our new event, "Coral Night". We will have a live band and Asian singers performing during the night. It is like a lounge where people can chill and have a sip. It will open on July 21.

```html
<!DOCTYPE html>
<html lang="en">
<head>
<meta charset="utf-8">
<title>Coral Night – Velora Nightclub</title>
<link rel="stylesheet" href="https://fonts.googleapis.com/css2?family=Poppins:wght@500;600&family=Marcellus&display=swap">
<style>
  :root {
    --night-black: #0b0609;
    --deep-plum: #2a0f22;
    --magenta-glow: #9a2f7a;
    --bulb-peach: #ffe3d8;
    --bulb-pink: #f2a6c9;
    --neon-pink: #ec9ed8;
    --soft-white: #f6eef3;
  }
  * { margin: 0; padding: 0; box-sizing: border-box; }
  html, body { width: 900px; height: 1200px; overflow: hidden; background: var(--night-black); }
  .poster {
    position: relative;
    width: 900px;
    height: 1200px;
    overflow: hidden;
    background:
      radial-gradient(ellipse 70% 45% at 55% 28%, var(--deep-plum) 0%, rgba(42,15,34,0.4) 55%, transparent 80%),
      linear-gradient(180deg, #120910 0%, var(--night-black) 60%, #070406 100%);
    font-family: "Marcellus", serif;
  }
  .backdrop-art {
    position: absolute;
    left: 150px; top: 60px;
    width: 700px; height: 560px;
    background:
      radial-gradient(ellipse 35% 30% at 60% 40%, rgba(154,47,122,0.55), transparent 70%),
      radial-gradient(ellipse 50% 40% at 40% 55%, rgba(110,30,90,0.35), transparent 75%);
    filter: blur(6px);
  }
  .light-burst {
    position: absolute;
    left: 60px; top: 560px;
    width: 780px; height: 200px;
    background:
      radial-gradient(ellipse 45% 12% at 50% 50%, rgba(255,220,240,0.7), transparent 70%),
      radial-gradient(ellipse 30% 40% at 50% 50%, rgba(236,158,216,0.35), transparent 75%);
  }
  .presenter {
    position: absolute;
    left: 45px; top: 38px;
    font-family: "Poppins", sans-serif;
    font-weight: 500;
    font-size: 22px;
    line-height: 1.15;
    color: var(--soft-white);
    text-transform: uppercase;
  }
  .event-title {
    position: absolute;
    left: 0; right: 0; top: 100px;
    text-align: center;
    font-family: "Poppins", sans-serif;
    font-weight: 600;
    font-size: 232px;
    line-height: 208px;
    letter-spacing: 6px;
    text-transform: uppercase;
  }
  .event-title span {
    display: block;
    color: var(--bulb-peach);
    background: radial-gradient(circle at 50% 50%, #fff8f2 0 3.5px, var(--bulb-pink) 5px, #c8779f 7px) 0 0 / 15px 15px;
    -webkit-background-clip: text;
    background-clip: text;
    -webkit-text-fill-color: transparent;
    filter: drop-shadow(0 0 10px rgba(236,158,216,0.8)) drop-shadow(0 0 24px rgba(154,47,122,0.7));
  }
  .event-date {
    position: absolute;
    left: 0; right: 0; top: 610px;
    text-align: center;
    font-size: 76px;
    color: var(--neon-pink);
    text-shadow: 0 0 12px rgba(236,158,216,0.6);
  }
  .event-details {
    position: absolute;
    left: 0; right: 0; top: 800px;
    text-align: center;
    color: var(--neon-pink);
    text-transform: uppercase;
    text-shadow: 0 0 8px rgba(236,158,216,0.5);
  }
  .event-details .live-music { font-size: 44px; }
  .event-details .doors { font-size: 52px; margin-top: 34px; }
</style>
</head>
<body>
  <main class="poster">
    <div class="backdrop-art" role="img" aria-label="Glowing magenta abstract swirl artwork behind the title"></div>
    <div class="light-burst" role="img" aria-label="Horizontal pink light flare behind the date"></div>
    <p class="presenter">Velora Nightclub<br>Presents</p>
    <h1 class="event-title"><span>Coral</span><span>Night</span></h1>
    <p class="event-date">July 21</p>
    <div class="event-details">
      <p class="live-music">Live music at 9:00 PM-11:00 PM</p>
      <p class="doors">Doors open at 8:00 PM</p>
    </div>
  </main>
</body>
</html>
```